NURSING: RISING PAST THE SHADOWED SILL

Size of the book cover: 140 x 215 mms

I need a cover for the 30,000 word book I have just written. It is a positive take on what I think nursing is and what it needs to be in the future. It is also my story of being nursed and of being a nurse.

My dream is that nurses honor themselves; that they look to the future with confidence and intelligence and that care continues to be delivered with compassionate person centeredness.

I define nursing as a professional workforce which, with probity, prevent or relieve distress; provide compassionate, safe, excellent care; and which contributes to the organization of healthcare.

The name comes from a Biblical parable Corlan 3:7-9. If a light is hidden under a bushel (basket) it is barely seen. If it is lit out from the basket it is clearly seen. As nurses we must continue to take up our mantel and ensure our light is seen and that it continues to shine the way we want it to.

As nurses we each take up our own lantern of caring, each in our own ways. To walk more brightly in our own paths of service.

The final design should show the specialness of nursing.

Target Market(s)

Nurses present, past and future

Industry/Entity Type

Healthcare

Font styles to use
Sans Serif
Other font styles liked:
• Whatever you think will suit

Colors
ec1f27
0393ce
9bcb3c

Requirements
Must have
• Be friendly, calming.
• NB: I am not sure whether the title should be in uppercase or not. Nursing could be uppercase and rising past the shadowed sill could be lower case. I leave it to you experienced people
Nice to have
• Something that depicts nursing...or is suggestive of nursing and the specialness of the work we do. How we bring our light to our patients as we 'hold them in the palms of out hands' and care for them. How they honor us by allowing us into their lives. Our rich past and out history allows us to be who we are today and we look to the future with confidence and hope
• I like rich colors, eg the color type you might find on a stained glass window in a church - rich emerald green or rich crimson red or the deep blue of a nurses cape
Should not have
• A dark cover
• clutter
• Religious overtone
• I have chosen three colors but they are not in the shading I would like - see above

```html
<!DOCTYPE html>
<html lang="en">
<head>
<meta charset="utf-8">
<title>Nursing: Rising past the shadowed sill — Book Cover</title>
<link rel="stylesheet" href="https://fonts.googleapis.com/css2?family=Titillium+Web:ital,wght@0,300;0,400;0,700;1,300&family=Josefin+Sans:wght@300;400&display=swap">
<style>
  :root {
    --stage: #000000;
    --turquoise: #3fc1cf;
    --sunny: #ece51b;
    --white: #ffffff;
    --ink: #1d1d1b;
    --band-green: #6cb53f;
    --lime-rule: #c2d62e;
    --body-ink: #1f3437;
  }
  * { box-sizing: border-box; margin: 0; padding: 0; }
  html, body {
    width: 1200px; height: 976px; overflow: hidden;
    background: var(--stage);
  }
  .spread {
    position: absolute; left: 74px; top: 89px;
    width: 1052px; height: 781px;
    background: var(--turquoise);
    font-family: "Titillium Web", sans-serif;
  }
  /* Back cover */
  .back-cover {
    position: absolute; left: 0; top: 0; width: 496px; height: 100%;
  }
  .blurb {
    position: absolute; left: 47px; top: 52px; width: 414px;
    color: var(--body-ink);
    font-size: 12.9px; line-height: 16px; font-weight: 400;
  }
  .blurb p { margin-bottom: 10.5px; }
  .blurb .book-title { color: var(--sunny); font-style: italic; font-weight: 300; }

  /* Spine */
  .spine {
    position: absolute; left: 496px; top: 0; width: 52px; height: 100%;
    border-right: 1px solid rgba(255,255,255,0.15);
  }
  .spine-title, .spine-author {
    position: absolute; left: 50%; transform: translateX(-50%);
    writing-mode: vertical-rl; white-space: nowrap;
  }
  .spine-title { top: 79px; font-size: 21.5px; line-height: 1; color: var(--white); font-weight: 300; }
  .spine-title strong { color: var(--sunny); font-weight: 700; }
  .spine-author {
    top: 557px; font-family: "Josefin Sans", sans-serif; font-weight: 400;
    font-size: 15px; color: var(--ink); letter-spacing: 0;
  }

  /* Front cover */
  .front-cover {
    position: absolute; left: 548px; top: 0; width: 504px; height: 100%;
    text-align: center;
  }
  .epigraph {
    position: absolute; left: 0; right: 0; top: 38px;
    color: var(--white); font-size: 15.6px; line-height: 21px; font-weight: 300;
  }
  .title-main {
    position: absolute; left: 0; right: 0; top: 140px;
    color: var(--sunny); font-weight: 700; font-size: 106px; line-height: 1; letter-spacing: 0;
  }
  .title-sub {
    position: absolute; left: 0; right: 0; top: 232px;
    color: var(--white); font-weight: 300; font-size: 33px; line-height: 1.2; letter-spacing: 0.5px;
  }
  .author-band {
    position: absolute; left: 0; right: 0; top: 313px; height: 50px;
    background: var(--band-green);
    display: flex; align-items: center; justify-content: center;
    font-family: "Josefin Sans", sans-serif; font-weight: 400; font-size: 26px; color: var(--ink);
    padding-top: 4px; word-spacing: 8px;
  }
  .cover-photo {
    position: absolute; left: 0; right: 0; top: 365px; height: 356px;
    background: linear-gradient(100deg, #e9f2f4 0%, #a8dbe0 30%, #e7ecee 55%, #7aa7cf 80%, #3e6fb5 100%);
  }
  .foreword {
    position: absolute; left: 0; right: 0; top: 735px;
    color: var(--white); font-size: 18px; font-weight: 300;
  }
  .base-rule {
    position: absolute; left: 0; right: 0; bottom: 0; height: 7px;
    background: var(--lime-rule);
  }
</style>
</head>
<body>
<main class="spread">
  <section class="back-cover">
    <div class="blurb">
      <p>Nursing is seldom expressed the way that it is in this book. It is written by a person who has been nursed or nursing all her life and it is recounted with honesty and candour. Every reader will find something to take from this narrative and nurses will no doubt see something of their own life mirrored in the many anecdotes and stories.</p>
      <p><span class="book-title">Nursing: Rising past the shadowed sill</span> is a book which brings into the light the authors rich experience of the world and work of nursing. Through its words it subtly challenges individual nurses to think deeply about what ‘being a nurse’ means to them.</p>
      <p>What nurses do is a very big deal. Nurses choose to be nurses. No one tells them they have to do it but for some reason they decide to. The people they care for honour them by allowing them into their lives at what can be the most vulnerable and dramatic times of their life. How nurses position themselves, how they ‘walk’ with their patients, how they connect and care for them has consequences both for those in their care and for themselves.</p>
      <p>One of nursing’s unique realities is that the work crosses normal social boundaries. It is work that is not easily talked about outside of nursing, and the support nurses provide for each other is important in enabling them to remain healthy and able.</p>
      <p>Nursing has a rich history. Elinor Marsh lit her lantern of caring more a then a century ago. The light from that lantern continues to glow and it is relit every moment of everyday by nurses all around the world as they go about their work.</p>
      <p>This book is more than just a story of nursing. It is the story and chronol­ogy of a professional life, intermingled with the telling of personal accounts and experiences. It also includes some special thoughts on nursing now and into the future. Nursing in the present day, presents many new challenges and opportunities. The workforce is one which adapts well to new ideas and situations.</p>
      <p>The future of nursing is in nurses hands and as such it can look to the future with confidence and pride.</p>
      <p>The writer salutes nurses everywhere.</p>
    </div>
  </section>

  <section class="spine">
    <div class="spine-title"><strong>NURSING :</strong> Rising past the shadowed sill</div>
    <div class="spine-author">MAREN&nbsp; HOLLOWAY</div>
  </section>

  <section class="front-cover">
    <p class="epigraph">“We each take up our own lantern of caring, each in our own<br>ways, to walk more brightly in our own path of service”</p>
    <h1 class="title-main">NURSING</h1>
    <p class="title-sub">Rising past the shadowed sill</p>
    <div class="author-band">MAREN HOLLOWAY</div>
    <div class="cover-photo" role="img" aria-label="Photograph of a smiling young nurse in teal scrubs with a stethoscope holding the hands of an elderly woman in a blue blouse"></div>
    <p class="foreword">Foreward by Edith Carrow RN</p>
    <div class="base-rule"></div>
  </section>
</main>
</body>
</html>
```